Harbin Cargo needs a business card design.

Design a double-sided business card for new freight business. On the front, would like to see our logo along with the following info:

Nathaniel Voskuhl
CEO/FOUNDER
617-552-0194
nathanielvoskuhl@harbin-cargo.example

On the reverse side, we would like to use the graphic image of our logo only without the Harbin Cargo name.

```html
<!DOCTYPE html>
<html lang="en">
<head>
<meta charset="utf-8">
<title>Harbin Cargo — Business Card</title>
<link rel="stylesheet" href="https://fonts.googleapis.com/css2?family=Montserrat:wght@500;700&family=Open+Sans:wght@400&display=swap">
<style>
  :root {
    --navy: #1c1957;
    --navy-pattern: #262476;
    --red: #c0202a;
    --white: #ffffff;
    --backdrop: #1d1d20;
    --rule: rgba(255,255,255,0.75);
  }
  * { box-sizing: border-box; margin: 0; padding: 0; }
  html, body { width: 1200px; height: 948px; overflow: hidden; }
  body {
    background: var(--backdrop);
    font-family: "Open Sans", sans-serif;
    position: relative;
  }
  .card {
    position: absolute;
    left: 300px;
    width: 600px;
    height: 343px;
    border-radius: 22px;
    overflow: hidden;
    background: var(--navy);
  }
  .card--back { top: 90px; }
  .card--front { top: 515px; }

  .back-pattern {
    position: absolute; inset: 0;
    background: linear-gradient(135deg, var(--navy-pattern), var(--navy) 70%);
  }
  .back-mark {
    position: absolute;
    right: 62px; top: 126px;
    width: 22px; height: 22px;
    background: var(--white);
  }

  .front-shape { position: absolute; inset: 0; }
  .front-brand {
    position: absolute;
    left: 40px; top: 158px;
    display: flex; align-items: center; gap: 10px;
    font-family: "Montserrat", sans-serif;
    font-weight: 700;
    font-size: 22px;
    letter-spacing: 2px;
    color: var(--navy);
    text-transform: uppercase;
    white-space: nowrap;
  }
  .front-brand .mark {
    width: 16px; height: 16px; background: var(--navy);
  }
  .contact {
    position: absolute;
    left: 345px; top: 66px;
    width: 230px;
    color: var(--white);
  }
  .contact__name {
    font-family: "Montserrat", sans-serif;
    font-weight: 700;
    font-size: 19px;
    letter-spacing: 0.5px;
    text-transform: uppercase;
    white-space: nowrap;
  }
  .contact__title {
    font-size: 12px;
    letter-spacing: 0.5px;
    margin-top: 4px;
  }
  .contact__rule {
    border: 0; border-top: 1px solid var(--rule);
    margin: 14px 0 14px;
  }
  .contact__list { list-style: none; font-size: 11px; }
  .contact__list li {
    display: flex; align-items: center; gap: 8px;
    margin-bottom: 7px; white-space: nowrap;
  }
  .contact__list svg { width: 11px; height: 11px; flex: none; fill: var(--white); }
</style>
</head>
<body>

<section class="card card--back">
  <div class="back-pattern" role="img" aria-label="Repeating tonal navy pattern of the company mark"></div>
  <div class="back-mark" aria-hidden="true"></div>
</section>

<section class="card card--front">
  <svg class="front-shape" viewBox="0 0 600 343" preserveAspectRatio="none">
    <path d="M0,38 Q80,24 160,34 Q305,66 322,343 H0 Z" fill="var(--white)"/>
    <path d="M0,20 Q80,6 168,16 Q322,50 338,343" fill="none" stroke="var(--red)" stroke-width="4"/>
  </svg>

  <div class="front-brand"><span class="mark"></span>Harbin Cargo</div>

  <div class="contact">
    <h1 class="contact__name">Nathaniel Voskuhl</h1>
    <p class="contact__title">CEO/FOUNDER</p>
    <hr class="contact__rule">
    <ul class="contact__list">
      <li>
        <svg viewBox="0 0 24 24"><path d="M6.6 10.8a15.1 15.1 0 0 0 6.6 6.6l2.2-2.2c.3-.3.7-.4 1-.2 1.1.4 2.3.6 3.6.6.6 0 1 .4 1 1V20c0 .6-.4 1-1 1C10.6 21 3 13.4 3 4c0-.6.4-1 1-1h3.5c.6 0 1 .4 1 1 0 1.3.2 2.5.6 3.6.1.3 0 .7-.2 1z"/></svg>
        617-552-0194
      </li>
      <li>
        <svg viewBox="0 0 24 24"><path d="M2 5h20v14H2z M2 5l10 8 10-8" fill="none" stroke="#fff" stroke-width="2"/></svg>
        nathanielvoskuhl@harbin-cargo.example
      </li>
      <li>
        <svg viewBox="0 0 24 24"><circle cx="12" cy="12" r="9" fill="none" stroke="#fff" stroke-width="2"/><path d="M3 12h18M12 3c3 3 3 15 0 18M12 3c-3 3-3 15 0 18" fill="none" stroke="#fff" stroke-width="1.6"/></svg>
        www.harbin-cargo.example
      </li>
    </ul>
  </div>
</section>

</body>
</html>
```